Logistics Website Design

See website https://tvarfreightglobal.com for theme and color details. Need the site to be re-done and reflect some of the designs shown in this list here: https://pinvora.com/tags/logistics-company-website

Target Market(s)

Logistics & Transportation

Industry/Entity Type

Logistics and Supply Chain

Coding

Coded - Design and coding required

Number of Pages Required

5+ page

Requirements
Must have
• Colors must match theme of logo. Looking for a sleek, interactive design.

```html
<!DOCTYPE html>
<html lang="en">
<head>
<meta charset="utf-8">
<title>Tvar Freight — Logistics</title>
<link href="https://fonts.googleapis.com/css2?family=Space+Grotesk:wght@500;600;700&family=Manrope:wght@400;500;600;700&display=swap" rel="stylesheet">
<style>
:root{
  --page:#ffffff;
  --bg:#150d0a;
  --bar:#1c1410;
  --card:#1e1510;
  --card-2:#2a1d16;
  --line:#2e211a;
  --orange:#f5845f;
  --orange-deep:#e8734d;
  --cream:#f7e4d7;
  --muted:#b9a699;
  --dim:#8e7b70;
  --black:#050302;
}
*{box-sizing:border-box;margin:0;padding:0}
html,body{width:1200px;height:2926px;overflow:hidden;background:var(--page)}
body{font-family:"Manrope",sans-serif;color:var(--cream)}
.site{position:absolute;left:28px;top:22px;width:1143px;height:2904px;background:var(--bg);overflow:hidden}
.abs{position:absolute}
.display{font-family:"Space Grotesk",sans-serif;font-weight:700;text-transform:uppercase;letter-spacing:-0.5px}

/* header */
.header{left:0;top:0;width:1143px;height:107px;background:var(--bar)}
.brand{left:72px;top:38px;display:flex;align-items:center;gap:10px;font-family:"Manrope",sans-serif;font-weight:800;font-size:17px;color:var(--orange);letter-spacing:.5px}
.brand-dot{width:26px;height:26px;border-radius:50%;background:var(--orange)}
.nav{left:403px;top:38px;display:flex;gap:22px;font-size:14px;font-weight:500;text-transform:uppercase;color:var(--cream)}
.nav a{color:inherit;text-decoration:none;padding-bottom:6px}
.nav a.active{color:var(--orange);border-bottom:2px solid var(--orange)}
.btn-quote{left:960px;top:39px;width:111px;height:30px;border-radius:5px;background:var(--orange);color:#2a140b;font-size:12px;font-weight:600;display:flex;align-items:center;justify-content:center;text-transform:uppercase}

/* hero */
.hero-photo{left:72px;top:198px;width:369px;height:554px;border-radius:12px;background:linear-gradient(180deg,#4f6a78 0%,#7d8a90 35%,#c79a84 55%,#3a3a3e 70%,#1b1c20 100%)}
.badge{left:486px;top:254px;height:24px;padding:0 11px;border:1px solid #5a3223;border-radius:12px;background:#241510;display:flex;align-items:center;gap:8px;font-size:10px;font-weight:700;letter-spacing:.8px;color:var(--orange)}
.badge i{width:6px;height:6px;border-radius:50%;background:var(--orange)}
.hero-title{left:486px;top:298px;width:620px;font-size:54px;line-height:68px}
.hero-title span{color:var(--orange)}
.hero-copy{left:486px;top:527px;width:580px;font-size:16px;line-height:26px;color:var(--muted)}
.btn{display:flex;align-items:center;justify-content:center;gap:10px;border-radius:6px;font-weight:700;font-size:16px}
.btn-track{left:486px;top:641px;width:221px;height:53px;background:var(--orange);color:#2a140b}
.btn-spec{left:722px;top:641px;width:197px;height:53px;background:var(--card-2);color:var(--cream);font-size:15px}

/* stats */
.stats{left:72px;top:841px;width:1000px;height:118px;border:3px solid var(--line);border-radius:10px;display:flex;gap:4px;background:var(--line)}
.stat{flex:1;background:var(--card);position:relative;padding:30px 0 0 30px}
.stat:first-child{border-radius:8px 0 0 8px}.stat:last-child{border-radius:0 8px 8px 0}
.stat-label{font-size:11px;font-weight:600;letter-spacing:2px;color:var(--muted);text-transform:uppercase}
.stat-value{font-family:"Space Grotesk",sans-serif;font-weight:600;font-size:32px;margin-top:6px}
.stat svg{position:absolute;right:28px;top:38px}

/* capabilities */
.cap-title{left:72px;top:1073px;font-size:42px;line-height:50px}
.cap-copy{left:72px;top:1132px;width:600px;font-size:14px;line-height:22px;color:var(--muted)}
.explore{left:910px;top:1153px;font-size:14px;font-weight:600;color:var(--orange);display:flex;align-items:center;gap:8px}
.ware{left:72px;top:1233px;width:659px;height:395px;border-radius:12px;overflow:hidden;background:linear-gradient(90deg,#6e2414 0%,#9b3e22 25%,#c46a44 50%,#9b3e22 75%,#5d1c10 100%)}
.ware-shade{position:absolute;inset:0;background:linear-gradient(180deg,rgba(21,13,10,0) 30%,rgba(21,13,10,.85) 85%,var(--bg) 100%)}
.ware-icon{position:absolute;left:36px;top:160px;width:48px;height:48px;border-radius:8px;background:rgba(90,45,30,.7);display:flex;align-items:center;justify-content:center}
.ware h3{position:absolute;left:36px;top:228px;font-family:"Space Grotesk",sans-serif;font-size:27px;font-weight:600}
.ware p{position:absolute;left:36px;top:276px;width:400px;font-size:14px;line-height:23px;color:#d9c6b9}
.tags{position:absolute;left:36px;top:345px;display:flex;gap:14px}
.tag{height:21px;padding:0 11px;background:#2a1b15;border-radius:3px;font-size:10px;font-weight:700;letter-spacing:1.2px;display:flex;align-items:center}
.priority{left:752px;top:1233px;width:319px;height:227px;border-radius:14px;background:linear-gradient(135deg,#3a2519,#2a1c15);padding:36px 37px}
.priority h3{font-family:"Space Grotesk",sans-serif;font-size:22px;font-weight:600}
.priority p{margin-top:16px;font-size:12px;line-height:20px;color:var(--muted)}
.btn-express{margin-top:10px;height:44px;border-radius:6px;background:var(--black);font-size:14px;font-weight:600;display:flex;align-items:center;justify-content:center}

.service{width:489px;height:173px;border-radius:12px;background:var(--card);padding:34px 22px}
.service h4{margin-top:14px;font-family:"Space Grotesk",sans-serif;font-size:18px;font-weight:600;letter-spacing:.3px}
.service .more{margin-top:14px;font-size:12px;font-weight:700;letter-spacing:1.5px;color:var(--orange)}

/* cta */
.cta{left:72px;top:2260px;width:1000px;height:398px;border-radius:28px;background:radial-gradient(circle at 5% 25%,#4a2a1c 0%,#2e1e16 45%,#241813 100%);text-align:center}
.cta h2{margin-top:72px;font-size:42px;line-height:44px}
.cta p{margin:30px auto 0;width:560px;font-size:16px;line-height:26px;color:var(--muted)}
.cta-actions{margin-top:40px;display:flex;justify-content:center;gap:15px}
.btn-start{width:235px;height:60px;background:var(--orange);color:#2a140b;font-size:17px;text-transform:uppercase;letter-spacing:-.5px}
.btn-ops{width:208px;height:60px;background:var(--black);color:var(--cream);font-size:15px;text-transform:uppercase;letter-spacing:-.5px}

/* footer */
.footer{left:0;top:2742px;width:1143px;height:162px;background:var(--bar)}
.footer-brand{position:absolute;left:43px;top:67px;font-size:17px;font-weight:700;color:var(--orange)}
.footer-note{position:absolute;left:43px;top:95px;font-size:10px;color:var(--dim);letter-spacing:-.2px}
.footer-links{position:absolute;left:420px;top:82px;display:flex;gap:29px;font-size:12px;color:var(--muted);text-transform:uppercase}
</style>
</head>
<body>
<div class="site">

  <header class="abs header">
    <div class="abs brand"><span class="brand-dot"></span>TVAR FREIGHT</div>
    <nav class="abs nav">
      <a class="active" href="#">Fleet</a><a href="#">Network</a><a href="#">Technology</a><a href="#">Tracking</a>
    </nav>
    <div class="abs btn-quote">Get Quote</div>
  </header>

  <div class="abs hero-photo" role="img" aria-label="Photo of a semi truck with a long trailer on a highway at sunset"></div>
  <div class="abs badge"><i></i>LIVE GLOBAL OPERATIONS ACTIVE</div>
  <h1 class="abs hero-title display">Bringing the <span>world</span><br>closer, one<br>delivery at a time</h1>
  <p class="abs hero-copy">Harnessing industrial precision through the AI Archive Engine. We don't just move freight; we orchestrate the kinetic pulse of global commerce with zero-latency routing.</p>
  <div class="abs btn btn-track">Initialize Tracking
    <svg width="16" height="16" viewBox="0 0 16 16" fill="none" stroke="#2a140b" stroke-width="1.8"><path d="M2 8h11M9 4l4 4-4 4"/></svg>
  </div>
  <div class="abs btn btn-spec">Fleet Specifications</div>

  <section class="abs stats">
    <div class="stat">
      <div class="stat-label">Active Accounts</div><div class="stat-value">20K+</div>
      <svg width="30" height="26" viewBox="0 0 30 26" fill="none" stroke="#c06a4b" stroke-width="2"><circle cx="11" cy="7" r="5"/><path d="M2 24c0-5 4-8 9-8s9 3 9 8z"/><path d="M18 3a5 5 0 010 9M22 16c4 1 6 4 6 8h-4"/></svg>
    </div>
    <div class="stat">
      <div class="stat-label">Fulfillment Rate</div><div class="stat-value">98%</div>
      <svg width="28" height="28" viewBox="0 0 28 28" fill="none" stroke="#c06a4b" stroke-width="2"><path d="M14 2l3 3h4v4l3 3-3 3v4h-4l-3 3-3-3H7v-4l-3-3 3-3V5h4z"/><path d="M9 14l3.5 3.5L19 11"/></svg>
    </div>
    <div class="stat">
      <div class="stat-label">Global Nodes</div><div class="stat-value">140+</div>
      <svg width="28" height="28" viewBox="0 0 28 28"><circle cx="14" cy="14" r="12" fill="#c06a4b"/><path d="M7 8c3 0 4 3 3 5s2 4 1 7M17 4c-1 3 2 4 4 4s2 4 5 4" fill="none" stroke="#1e1510" stroke-width="2"/></svg>
    </div>
  </section>

  <h2 class="abs cap-title display">Core Capabilities</h2>
  <p class="abs cap-copy">Our infrastructure is built for high-velocity distribution and archival-grade security across every transit medium.</p>
  <div class="abs explore">EXPLORE NETWORK
    <svg width="18" height="14" viewBox="0 0 18 14" fill="none" stroke="#f5845f" stroke-width="1.8"><path d="M1 7h15M11 2l5 5-5 5"/></svg>
  </div>

  <article class="abs ware">
    <div role="img" aria-label="Photo of a warehouse aisle with tall orange racks and robotic arms" style="position:absolute;inset:0"></div>
    <div class="ware-shade"></div>
    <div class="ware-icon"><svg width="22" height="22" viewBox="0 0 22 22" fill="none" stroke="#f5845f" stroke-width="2"><rect x="2" y="3" width="18" height="5" rx="1"/><path d="M4 8v11h14V8M9 12h4"/></svg></div>
    <h3>Automated Warehousing</h3>
    <p>Smart archival storage units equipped with robotic sorting and climate-controlled environments for sensitive cargo.</p>
    <div class="tags"><span class="tag">ROBOTIC SORTING</span><span class="tag">24/7 MONITORING</span></div>
  </article>

  <article class="abs priority">
    <h3>Priority Transit</h3>
    <p>Direct-to-destination protocols for time-critical assets using our proprietary air-corridors.</p>
    <div class="btn-express">Schedule Express</div>
  </article>

  <article class="abs service" style="left:72px;top:1692px">
    <svg width="40" height="28" viewBox="0 0 40 28" fill="none" stroke="#f5a283" stroke-width="1.6"><path d="M3 20V10h9l5-6h6v16zM23 12h14v8H23M12 10V4"/><circle cx="9" cy="22" r="3"/><circle cx="30" cy="22" r="3"/></svg>
    <h4>Flatbed Transportation</h4><div class="more">LEARN MORE →</div>
  </article>
  <article class="abs service" style="left:582px;top:1692px">
    <svg width="44" height="28" viewBox="0 0 44 28" fill="none" stroke="#f5a283" stroke-width="1.6"><path d="M3 20V6h10l4 5v9zM17 11h24v9H17M6 9h5"/><circle cx="9" cy="22" r="3"/><circle cx="34" cy="22" r="3"/></svg>
    <h4>Step Deck Transportation</h4><div class="more">LEARN MORE →</div>
  </article>
  <article class="abs service" style="left:72px;top:1887px">
    <svg width="56" height="28" viewBox="0 0 56 28" fill="none" stroke="#f5a283" stroke-width="1.6"><path d="M3 6h34v14H3zM37 10h9l6 5v5H37M8 10h24M8 14h24"/><circle cx="10" cy="22" r="3"/><circle cx="44" cy="22" r="3"/></svg>
    <h4>Dry Van Transportation</h4><div class="more">LEARN MORE →</div>
  </article>
  <article class="abs service" style="left:582px;top:1887px">
    <svg width="56" height="28" viewBox="0 0 56 28" fill="none" stroke="#f5a283" stroke-width="1.6"><path d="M3 14h36v6H3zM39 8h8l6 6v6H39zM8 14V9h22v5"/><circle cx="9" cy="22" r="3"/><circle cx="46" cy="22" r="3"/></svg>
    <h4>Heavy Haul Transportation</h4><div class="more">LEARN MORE →</div>
  </article>

  <section class="abs cta">
    <h2 class="display">Ready to scale your<br>network?</h2>
    <p>Integrate with the world's most precise logistics archive and redefine your delivery standard.</p>
    <div class="cta-actions">
      <div class="btn btn-start">Start Integration</div>
      <div class="btn btn-ops">Talk to Operations</div>
    </div>
  </section>

  <footer class="abs footer">
    <div class="footer-brand">TVAR FREIGHT</div>
    <div class="footer-note">© 2026. AN INDEPENDENT AGENT OF HALVERN CARTER LLC.</div>
    <div class="footer-links"><span>Terms of Service</span><span>Privacy Policy</span><span>Global Compliance</span><span>Carrier Portal</span><span>Contact Support</span></div>
  </footer>

</div>
</body>
</html>
```